Harold The Realtor Business Card Design

I need a new card design for my real estate business in Seattle Wa. I am interested in a unique design. My business revolves around my personal services and I want the card to show professionalism, creativity and good execution. I specialize in residential real estate in Maple ridge / downtown neighborhoods. The card is my first impression on may of my clients and in the service industry any time you can stand out from the crowd and make an impression will go a long way.

Target Market(s)

I will be handing the card to prospects/ potential buyers and sellers of residential real estate.

Industry/Entity Type

Real Estate Agent

Contact Information for Business Card

Email: Info@Haroldtherealtor.com Website: HaroldtheRealtor.com Cell phone: 206-555-0184 Fax 206-555-0127

Font styles to use
Sans Serif

Colors
0255a3
ffc214

Requirements
Must have
• I will need to have my firms logo "Keystone 8" and my logo "HTR" on the business card. I would like to have my firms logo smaller then mine. I would also like to have my photo on the card. By business colors are gold and white with blue accents.
Nice to have
• It would be nice to have a unique shape or feel (texture) rather then your standard business card. I saw cardly press had metal cards which could be interesting.

```html
<!DOCTYPE html>
<html lang="en">
<head>
<meta charset="utf-8">
<title>Harold The Realtor – Business Card</title>
<link href="https://fonts.googleapis.com/css2?family=Archivo:wght@400;800&display=swap" rel="stylesheet">
<style>
  :root {
    --page: #e9e9ec;
    --card: #fbfbfb;
    --card-shade: #efefef;
    --gold: #8f6c2c;
    --gold-dark: #6e5120;
    --blue: #4f86d6;
    --ink: #3a3a3a;
    --muted: #7c7c7c;
    --white: #ffffff;
  }
  * { box-sizing: border-box; margin: 0; padding: 0; }
  html, body { width: 1200px; height: 997px; overflow: hidden; }
  body {
    background: var(--page);
    font-family: "Archivo", Arial, sans-serif;
    position: relative;
  }
  .card {
    position: absolute;
    left: 320px;
    width: 560px;
    height: 320px;
    background: linear-gradient(160deg, var(--card) 55%, var(--card-shade));
    border-radius: 0 60px 0 60px;
    overflow: hidden;
    box-shadow: 0 10px 30px rgba(0,0,0,.18);
  }
  .card--back { top: 100px; }
  .card--front { top: 500px; }

  /* wordmark replacing the client mark */
  .wordmark {
    position: absolute;
    display: flex;
    align-items: center;
    gap: 12px;
    color: var(--gold);
    font-weight: 800;
    line-height: 1;
  }
  .wordmark__square {
    width: 18px; height: 18px; background: var(--gold);
  }
  .wordmark__name { display: flex; flex-direction: column; }
  .wordmark__name small { font-size: .42em; letter-spacing: .2em; margin-top: 6px; }

  .card--back .wordmark { left: 44px; top: 128px; font-size: 34px; }
  .card--front .wordmark { left: 40px; top: 104px; font-size: 46px; }

  .wordmark-rule {
    position: absolute; height: 2px; background: var(--gold);
  }
  .card--back .wordmark-rule { left: 44px; top: 218px; width: 150px; }
  .card--front .wordmark-rule { left: 40px; top: 206px; width: 190px; }

  /* back side */
  .divider {
    position: absolute; left: 262px; top: 118px; width: 2px; height: 80px;
    background: linear-gradient(var(--card), var(--blue), var(--card));
  }
  .contact {
    position: absolute; left: 282px; top: 118px;
    list-style: none; font-size: 13px; color: var(--ink);
  }
  .contact li { display: flex; align-items: center; gap: 10px; height: 26px; }
  .contact svg { width: 16px; height: 16px; flex: none; }

  .firm {
    position: absolute; right: 34px; top: 26px;
    display: flex; align-items: center; gap: 8px;
    color: var(--muted); font-size: 17px; font-weight: 400;
  }
  .firm__circle { width: 14px; height: 14px; border-radius: 50%; background: var(--muted); }
  .firm__tag { position: absolute; right: 0; top: 22px; font-size: 6px; letter-spacing: .2em; }

  /* front side */
  .web-band {
    position: absolute; left: 0; bottom: 0; width: 100%; height: 68px;
    background: linear-gradient(90deg, var(--gold-dark), var(--gold));
  }
  .web-band__url {
    position: absolute; left: 40px; top: 24px;
    color: var(--white); font-size: 16px; font-weight: 800; letter-spacing: .16em;
  }
  .portrait {
    position: absolute; right: 0; top: 30px; width: 220px; height: 290px;
    background: linear-gradient(180deg, #6b4a36 0%, #4a3a33 35%, #273552 65%, #1f2a44 100%);
    border-radius: 0 0 0 0;
  }
</style>
</head>
<body>

  <section class="card card--back" aria-label="Business card back">
    <div class="firm">
      <span class="firm__circle"></span>
      <span>Keystone 8</span>
      <span class="firm__tag">REAL ESTATE</span>
    </div>

    <div class="wordmark">
      <span class="wordmark__square"></span>
      <span class="wordmark__name">Harold<small>THE REALTOR</small></span>
    </div>
    <div class="wordmark-rule"></div>

    <div class="divider"></div>
    <ul class="contact">
      <li>
        <svg viewBox="0 0 16 16"><circle cx="8" cy="8" r="8" fill="var(--blue)"/><path d="M5 4.5l1.6-.5 1 2-1 .8a5 5 0 0 0 2.6 2.6l.8-1 2 1-.5 1.6c-3.4.3-6.8-3.1-6.5-6.5z" fill="#fff"/></svg>
        <span>206-555-0184</span>
      </li>
      <li>
        <svg viewBox="0 0 16 16"><circle cx="8" cy="8" r="8" fill="var(--blue)"/><rect x="4.5" y="6" width="7" height="5" fill="#fff"/><rect x="5.5" y="4" width="5" height="2" fill="#fff"/></svg>
        <span>206-555-0127</span>
      </li>
      <li>
        <svg viewBox="0 0 16 16"><circle cx="8" cy="8" r="8" fill="var(--blue)"/><rect x="4" y="5.5" width="8" height="5.5" fill="#fff"/><path d="M4 5.5l4 3 4-3" stroke="var(--blue)" fill="none"/></svg>
        <span>Info@Haroldtherealtor.com</span>
      </li>
    </ul>
  </section>

  <section class="card card--front" aria-label="Business card front">
    <div class="web-band">
      <span class="web-band__url">www.HaroldtheRealtor.com</span>
    </div>

    <div class="wordmark">
      <span class="wordmark__square"></span>
      <span class="wordmark__name">Harold<small>THE REALTOR</small></span>
    </div>
    <div class="wordmark-rule"></div>

    <div class="portrait" role="img" aria-label="Portrait photo of the realtor in a navy suit and pink tie"></div>
  </section>

</body>
</html>
```